Business Card Design Project

We are looking for a new business card design for a Drilling company in WA, Australia.

We are in between offices, however require a design in the meantime due to some upcoming events with our basic information.

The Logo for our company is Blue and Grey and would like this colour scheme throughout.

We are quite a new company so would like a memorable design that stands out and communicates a strong commitment to safety, quality of work and performance.

The company name is Ridgeback Boring Works (RBW)

The details to be included are as follows:

Martin Calloway
Managing Director
m.0481639027
e.martin@rbwgroup.com.au

Simon Calloway
Director
m.0429561384
e.simon@rbwgroup.com.au

Industry/Entity Type

Events

Requirements
Must have
• Under the Logo, we would like 'Western Australia'

```html
<!DOCTYPE html>
<html lang="en">
<head>
<meta charset="utf-8">
<title>Ridgeback Boring Works – Business Card</title>
<link rel="stylesheet" href="https://fonts.googleapis.com/css2?family=Open+Sans:wght@400;600;700&display=swap">
<style>
  :root {
    --navy: #0f2170;
    --grey: #5f5f61;
    --grey-light: #8a8a8c;
    --white: #ffffff;
    --backdrop: #e7e7ea;
  }
  * { margin: 0; padding: 0; box-sizing: border-box; }
  html, body { width: 1200px; height: 901px; overflow: hidden; }
  body {
    background: var(--backdrop);
    font-family: "Open Sans", Arial, sans-serif;
    position: relative;
  }
  .card {
    position: absolute;
    width: 540px;
    height: 310px;
    border-radius: 18px;
    overflow: hidden;
    box-shadow: 0 6px 18px rgba(0,0,0,0.18);
  }
  .card-front { left: 40px; top: 296px; background: var(--white); }
  .card-back { left: 620px; top: 296px; background: var(--navy); }

  .brand { position: absolute; display: flex; flex-direction: column; }
  .brand-row { display: flex; align-items: center; gap: 10px; }
  .brand-square { width: 14px; height: 14px; }
  .brand-name { font-weight: 700; font-size: 21px; line-height: 1.1; }
  .brand-region { font-size: 11px; letter-spacing: 2px; margin-top: 4px; }

  .card-front .brand { left: 34px; top: 34px; }
  .card-front .brand-square { background: var(--navy); }
  .card-front .brand-name { color: var(--navy); }
  .card-front .brand-region { color: var(--grey); padding-left: 24px; }

  .card-back .brand { right: 34px; bottom: 40px; align-items: flex-end; }
  .card-back .brand-square { background: var(--white); }
  .card-back .brand-name { color: var(--white); font-size: 24px; }
  .card-back .brand-region { color: var(--white); }

  .footer-band { position: absolute; left: 0; bottom: 0; width: 540px; height: 40px; }

  .contact {
    position: absolute;
    right: 30px;
    bottom: 52px;
    text-align: right;
  }
  .person-name { color: var(--navy); font-weight: 700; font-size: 19px; }
  .person-title { color: var(--grey); font-size: 12.5px; margin-bottom: 14px; }
  .contact-list { display: flex; justify-content: flex-end; gap: 10px; }
  .contact-lines { display: flex; flex-direction: column; gap: 4px; color: var(--grey); font-size: 12.5px; line-height: 16px; }
  .contact-divider { width: 1px; background: var(--grey-light); }
  .contact-icons { display: flex; flex-direction: column; gap: 4px; }
  .contact-icons svg { width: 14px; height: 16px; display: block; }
</style>
</head>
<body>

  <section class="card card-front" aria-label="Business card front">
    <div class="brand">
      <div class="brand-row">
        <span class="brand-square"></span>
        <span class="brand-name">Ridgeback Boring Works</span>
      </div>
      <span class="brand-region">Western Australia</span>
    </div>

    <div class="contact">
      <div class="person-name">Martin Calloway</div>
      <div class="person-title">Managing Director</div>
      <div class="contact-list">
        <div class="contact-lines">
          <span>0481639027</span>
          <span>martin@rbwgroup.com.au</span>
          <span>www.rbwgroup.com.au</span>
        </div>
        <span class="contact-divider"></span>
        <div class="contact-icons">
          <svg viewBox="0 0 14 16" aria-label="Mobile"><g fill="var(--navy)"><rect x="1" y="10" width="2" height="3"/><rect x="4.5" y="8" width="2" height="5"/><rect x="8" y="6" width="2" height="7"/><rect x="11.5" y="4" width="2" height="9"/></g></svg>
          <svg viewBox="0 0 14 16" aria-label="Email"><rect x="1" y="4" width="12" height="8" fill="none" stroke="var(--navy)" stroke-width="1.4"/><path d="M1 4 L7 9 L13 4" fill="none" stroke="var(--navy)" stroke-width="1.4"/></svg>
          <svg viewBox="0 0 14 16" aria-label="Website"><circle cx="7" cy="8" r="5.5" fill="none" stroke="var(--navy)" stroke-width="1.3"/><ellipse cx="7" cy="8" rx="2.4" ry="5.5" fill="none" stroke="var(--navy)" stroke-width="1"/><line x1="1.5" y1="8" x2="12.5" y2="8" stroke="var(--navy)" stroke-width="1"/></svg>
        </div>
      </div>
    </div>

    <svg class="footer-band" viewBox="0 0 540 40" aria-hidden="true">
      <polygon points="0,12 330,12 330,40 0,40" fill="var(--navy)"/>
      <polygon points="330,20 540,20 540,40 330,40" fill="var(--grey)"/>
    </svg>
  </section>

  <section class="card card-back" aria-label="Business card back">
    <div class="brand">
      <div class="brand-row">
        <span class="brand-square"></span>
        <span class="brand-name">Ridgeback Boring Works</span>
      </div>
      <span class="brand-region">Western Australia</span>
    </div>
  </section>

</body>
</html>
```